e social network with e-commerce website

Wefolkly.net is an online social network with e-commerce capabilities designed to connect Muslims with their peers. It also connects Halal suppliers with consumers, promoting authentic Halal standards of living through a trusted verification process by actual authorities of the Muslim Community.Products: E-commerce, Search Engine,Social Network,Online Shopping,e-Verification for Halal products and services

Industry/Entity Type

E-Commerce

```html
<!DOCTYPE html>
<html lang="en">
<head>
<meta charset="utf-8">
<title>Wefolkly.net — Founding (continued)</title>
<link rel="stylesheet" href="https://fonts.googleapis.com/css2?family=Arimo:ital,wght@0,400;0,700;1,400&family=Oswald:wght@400;500&display=swap">
<style>
  :root{
    --lime:#8ce40c;
    --pale:#e5f6c6;
    --white:#ffffff;
    --ink:#1a1a1a;
    --bar:#3d7d14;
    --header-a:#4fa817;
    --header-b:#9bdc4a;
    --nav-bg:#f3f9ea;
    --nav-ink:#5a9c1a;
    --link:#5aa51b;
    --accent:#7cc82a;
    --muted:#777777;
    --line:#dde7d0;
    --filter-bg:#f5fae6;
    --footer:#3e701b;
    --star:#f2b51d;
    --modal-frame:#7f8c80;
    --modal-head:#222222;
    --map-a:#d9d6cf;
    --map-b:#c3d6e4;
  }
  *{box-sizing:border-box;margin:0;padding:0}
  html,body{width:1200px;height:933px;overflow:hidden}
  body{background:var(--lime);font-family:"Arimo",Arial,sans-serif;color:var(--ink)}
  .page{position:relative;width:1080px;height:840px;transform:scale(1.11111);transform-origin:0 0}

  .page__panel{position:absolute;left:0;top:0;width:695px;height:828px;background:var(--pale)}
  .feedback-tab{position:absolute;left:12px;top:350px;width:16px;height:48px;background:#e9f4fb;border:1px solid #7aa7c7;
    font-size:7px;font-weight:700;color:#2f5f86;writing-mode:vertical-rl;transform:rotate(180deg);display:flex;align-items:center;justify-content:center}

  .site{position:absolute;left:65px;top:12px;width:577px;height:803px;background:var(--white);font-size:7px;overflow:hidden}
  .abs{position:absolute}

  .topbar{left:0;top:0;width:577px;height:23px;background:var(--bar)}
  .topbar__search{left:5px;top:5px;width:145px;height:13px;background:#fff;border-radius:7px;color:#aaa;font-size:6px;padding:2px 6px}
  .topbar__icon{top:7px;width:9px;height:9px;background:#fff;border-radius:2px}
  .topbar__badge{left:210px;top:2px;width:8px;height:8px;background:#e02020;color:#fff;font-size:5px;text-align:center;line-height:8px;border-radius:1px}
  .topbar__menu{top:7px;color:#fff;font-weight:700;font-size:7px}

  .banner{left:0;top:23px;width:577px;height:57px;background:linear-gradient(180deg,var(--header-a),var(--header-b))}
  .brand{left:10px;top:29px;font-size:40px;font-weight:700;color:#eaf7d4;letter-spacing:-1px;line-height:1}
  .seal{top:28px;width:22px;height:22px;border-radius:50%;background:#f3f3ea;border:2px solid #c8a84a}
  .seal--second{border-color:#3f7f9c}
  .verified{left:475px;top:56px;width:100px;color:#1f3f10;font-size:5px;line-height:1.35;font-weight:700;text-transform:uppercase}

  .nav{left:0;top:80px;width:577px;height:22px;background:var(--nav-bg);border-bottom:1px solid var(--line);
    display:flex;gap:9px;padding:5px 10px;font-family:"Oswald",Arial,sans-serif;font-size:8.5px;color:var(--nav-ink);font-weight:500}

  .crumb{left:8px;top:110px;color:var(--link);font-size:7px}
  .btn-add{left:493px;top:107px;width:78px;height:14px;border:1px solid #bbb;border-radius:2px;background:#f7f7f7;font-weight:700;font-size:6.5px;text-align:center;line-height:12px}

  .side{left:7px;top:134px;width:103px}
  .side__item{height:12.5px;line-height:12.5px;padding-left:1px;color:#333}
  .side__item--active{background:var(--accent);color:#fff;font-weight:700}
  .side__head{margin-top:16px;font-family:"Oswald",Arial,sans-serif;color:var(--nav-ink);font-size:8px;border-bottom:2px solid var(--accent);padding-bottom:2px;margin-bottom:4px}
  .side__cat{height:13px;line-height:12px;border-bottom:1px solid var(--line);color:#333}

  .listing-search{left:117px;top:133px;width:91px;height:13px;border:1px solid #ccc;border-radius:2px;color:#bbb;font-size:5.5px;padding:2px 4px}
  .sorter{left:380px;top:135px;font-size:6px;color:var(--muted)}
  .sorter b{color:#333;font-weight:400}
  .section-title{left:117px;top:160px;font-family:"Oswald",Arial,sans-serif;font-size:9.5px;color:#333}

  .tag{width:36px;height:11px;background:#222;color:#fff;font-size:6px;line-height:11px;padding-left:4px}
  .thumb{width:70px;height:43px}
  .stars{color:var(--star);font-size:8px;letter-spacing:-0.5px}
  .reviews{font-size:6px;color:#555}
  .avatar{width:28px;height:30px;background:linear-gradient(160deg,#9a8a7a,#5b4f47)}
  .mini{width:18px;height:18px;background:linear-gradient(160deg,#a5958a,#5d524b)}
  .title{color:var(--link);font-weight:700;font-size:7px}
  .price{font-weight:700;font-size:6.5px}
  .meta{color:var(--muted);font-size:6px}
  .desc{font-size:6px;color:#333;line-height:1.6;width:175px}
  .more{color:var(--link);font-size:6px}
  .actions{color:var(--link);font-size:6px}
  .count{width:22px;height:10px;border:1px solid #ccc;border-radius:2px;font-size:5.5px;text-align:right;padding-right:3px;line-height:9px;background:#f8f8f8}
  .divider{left:117px;width:300px;height:1px;background:var(--line)}

  .filter{left:430px;top:181px;width:139px;height:444px;background:var(--filter-bg)}
  .filter__head{left:430px;top:181px;width:139px;height:14px;background:var(--accent);color:#fff;font-family:"Oswald",Arial,sans-serif;font-size:7.5px;padding:2px 3px}
  .filter__label{left:432px;font-size:6px;color:#333}
  .filter__input{left:482px;width:85px;height:11px;border:1px solid #ccc;background:#fff;font-size:5.5px;padding:1px 3px}

  .modal{position:absolute;left:228px;top:325px;width:439px;height:267px;background:var(--modal-frame);border-radius:3px;padding:8px;font-size:7px}
  .modal__inner{position:relative;width:100%;height:100%;background:#f4f4f4}
  .modal__head{height:18px;background:var(--modal-head);color:#fff;font-weight:700;font-size:7px;padding:5px 4px}
  .modal__field{top:24px;height:12px;border:1px solid #ccc;background:#fff;font-size:6px;color:#777;padding:1px 3px}
  .modal__map{left:9px;top:40px;width:405px;height:175px;background:linear-gradient(135deg,var(--map-a),#e7e3d8 55%,var(--map-b))}
  .modal__close{right:6px;top:225px;width:30px;height:12px;border:1px solid #bbb;border-radius:2px;background:#fff;font-size:6px;text-align:center;line-height:10px}

  .footer{left:0;top:768px;width:577px;height:35px;background:var(--footer);color:#fff;font-size:6.5px;font-weight:700;padding:8px 11px;display:flex;justify-content:space-between}
  .footer__links{display:flex;gap:8px}

  .copy{position:absolute;left:747px;top:138px;width:276px;color:var(--white)}
  .copy__title{font-size:18px;font-weight:700;margin-bottom:13px}
  .copy__title span{font-weight:400}
  .copy p{font-size:14.6px;line-height:19.4px;margin-bottom:19px;hyphens:auto;-webkit-hyphens:auto}
  .folio{position:absolute;left:1038px;top:795px;font-size:14px;color:var(--ink)}
</style>
</head>
<body>
<div class="page">
  <div class="page__panel"></div>
  <div class="feedback-tab">Feedback</div>

  <div class="site">
    <div class="abs topbar"></div>
    <div class="abs topbar__search">Search...</div>
    <div class="abs topbar__icon" style="left:162px"></div>
    <div class="abs topbar__icon" style="left:182px"></div>
    <div class="abs topbar__icon" style="left:202px"></div>
    <div class="abs topbar__badge">6</div>
    <div class="abs topbar__menu" style="left:483px">Profile ▾</div>
    <div class="abs topbar__menu" style="left:525px">Account ▾</div>

    <div class="abs banner"></div>
    <div class="abs brand">Wefolkly</div>
    <div class="abs seal" style="left:528px"></div>
    <div class="abs seal seal--second" style="left:552px"></div>
    <div class="abs verified">Verified by<br>The Halal Standards Institute</div>

    <div class="abs nav">
      <span>HOME</span><span>FRIENDS</span><span>MEMBERS</span><span>PAGES</span><span>BLOGS</span><span>MARKETPLACE</span><span>PHOTOS</span><span>FORUM</span><span>POLLS</span><span>VIDEOS</span><span>EVENTS</span><span>STORE</span><span>COURSES</span><span>ASKING</span><span>MORE</span>
    </div>

    <div class="abs crumb"><span style="color:#333">⌂</span> Marketplace</div>
    <div class="abs btn-add">+ Add New Listing</div>

    <div class="abs side">
      <div class="side__item">All Listings</div>
      <div class="side__item">My Listings</div>
      <div class="side__item">Listing Invites</div>
      <div class="side__item">Friends' Listings</div>
      <div class="side__item side__item--active">Map View</div>
      <div class="side__head">CATEGORIES</div>
      <div class="side__cat">Community</div>
      <div class="side__cat">Houses</div>
      <div class="side__cat">Jobs</div>
      <div class="side__cat">Pets</div>
      <div class="side__cat">Rentals</div>
      <div class="side__cat">Services</div>
      <div class="side__cat">Stuff</div>
      <div class="side__cat">Tickets</div>
      <div class="side__cat">Vehicle</div>
    </div>

    <div class="abs listing-search">Search Listings...</div>
    <div class="abs sorter">Sort: <b>Latest ▾</b> &nbsp;Show: <b>10 per page ▾</b> &nbsp;When: <b>All Time ▾</b></div>
    <div class="abs section-title">MAP VIEW</div>

    <div class="abs tag" style="left:112px;top:178px">Featured</div>
    <div class="abs thumb" role="img" aria-label="Photo of a yacht interior" style="left:118px;top:187px;background:linear-gradient(135deg,#d9dde0,#6c7a86)"></div>
    <div class="abs stars" style="left:127px;top:233px">★★★★★</div>
    <div class="abs reviews" style="left:135px;top:244px">1 Review(s)</div>
    <div class="abs avatar" role="img" aria-label="Seller profile photo" style="left:200px;top:186px"></div>
    <div class="abs title" style="left:233px;top:188px">Yacht</div>
    <div class="abs price" style="left:235px;top:198px">$1,000,000.00</div>
    <div class="abs meta" style="left:233px;top:210px">December 3, 2014 · Niran · Thailand</div>
    <div class="abs desc" style="left:233px;top:219px">Luxury cruising yacht, fully equipped,<br>ready to sail this season</div>
    <div class="abs more" style="left:233px;top:241px">See More</div>
    <div class="abs actions" style="left:233px;top:262px">Like · Comment · Share · Print · Review ·</div>
    <div class="abs actions" style="left:233px;top:271px">Contact Seller</div>
    <div class="abs mini" role="img" aria-label="Friend avatar" style="left:235px;top:286px"></div>
    <div class="abs mini" role="img" aria-label="Friend avatar" style="left:256px;top:286px"></div>
    <div class="abs count" style="left:385px;top:290px">2</div>
    <div class="abs actions" style="left:235px;top:306px">View all 1 comments</div>
    <div class="abs divider" style="top:331px"></div>

    <div class="abs tag" style="left:112px;top:334px">Featured</div>
    <div class="abs thumb" role="img" aria-label="Listing photo" style="left:118px;top:343px;background:linear-gradient(135deg,#8fc9d8,#3e6f7c)"></div>
    <div class="abs stars" style="left:127px;top:392px">★★★★★</div>
    <div class="abs reviews" style="left:135px;top:403px">1 Review(s)</div>

    <div class="abs tag" style="left:112px;top:478px">Featured</div>
    <div class="abs thumb" role="img" aria-label="Listing photo" style="left:118px;top:487px;background:linear-gradient(135deg,#eadfe6,#a58a9a)"></div>
    <div class="abs stars" style="left:127px;top:530px">★★★★★</div>
    <div class="abs reviews" style="left:135px;top:541px">2 Review(s)</div>
    <div class="abs actions" style="left:233px;top:569px">Contact Seller</div>
    <div class="abs mini" role="img" aria-label="Friend avatar" style="left:235px;top:586px"></div>
    <div class="abs mini" role="img" aria-label="Friend avatar" style="left:257px;top:586px"></div>
    <div class="abs mini" role="img" aria-label="Friend avatar" style="left:279px;top:586px"></div>
    <div class="abs count" style="left:385px;top:590px">4</div>
    <div class="abs divider" style="top:614px"></div>

    <div class="abs tag" style="left:112px;top:618px">Featured</div>
    <div class="abs thumb" role="img" aria-label="Photo of an aquarium tunnel" style="left:118px;top:624px;height:42px;background:linear-gradient(135deg,#7fd2e2,#0f5c70)"></div>
    <div class="abs stars" style="left:127px;top:667px">★★★★★</div>
    <div class="abs reviews" style="left:135px;top:678px">1 Review(s)</div>
    <div class="abs avatar" role="img" aria-label="Seller profile photo" style="left:201px;top:623px"></div>
    <div class="abs title" style="left:233px;top:623px;width:185px">Riverside Plaza: ฿245 for Admission to Deep Blue Gallery at Harbor Aquarium for One (฿450 Value).</div>
    <div class="abs price" style="left:235px;top:644px">$8.00</div>
    <div class="abs meta" style="left:233px;top:656px">October 11, 2014 · Kai Porter · Thailand</div>
    <div class="abs desc" style="left:233px;top:668px;width:180px">The Deal ฿245 for admission to Deep Blue Gallery for one (฿450 value) Tel.: (02) 555-0142 Operating hours: <span style="color:var(--link)">10 a.m.–9 p.m.</span> (last admission at 8 p.m.)</div>
    <div class="abs actions" style="left:233px;top:707px">Like · Comment · Share · Print · Review ·</div>
    <div class="abs actions" style="left:233px;top:716px">Contact Seller</div>
    <div class="abs mini" role="img" aria-label="Friend avatar" style="left:235px;top:731px"></div>
    <div class="abs mini" role="img" aria-label="Friend avatar" style="left:257px;top:731px"></div>
    <div class="abs mini" role="img" aria-label="Friend avatar" style="left:279px;top:731px"></div>
    <div class="abs count" style="left:385px;top:735px">3</div>

    <div class="abs filter"></div>
    <div class="abs filter__head">SEARCH FILTER</div>
    <div class="abs filter__label" style="top:205px">Keywords:</div><div class="abs filter__input" style="top:202px"></div>
    <div class="abs filter__label" style="top:222px">Sort:</div><div class="abs filter__input" style="top:219px;width:60px">Latest ▾</div>
    <div class="abs filter__label" style="top:239px">Show:</div><div class="abs filter__input" style="top:236px;width:45px">10 per page ▾</div>
    <div class="abs filter__label" style="top:256px">When:</div><div class="abs filter__input" style="top:253px;width:45px">All Time ▾</div>
    <div class="abs filter__label" style="top:273px">Street:</div><div class="abs filter__input" style="top:270px"></div>
    <div class="abs filter__label" style="top:289px">City:</div><div class="abs filter__input" style="top:286px"></div>
    <div class="abs filter__label" style="top:305px">Zip/Postal<br>Code:</div><div class="abs filter__input" style="top:302px"></div>
    <div class="abs meta" style="left:467px;top:568px">October 11, 2014 · Kai Porter · Thailand</div>
    <div class="abs stars" style="left:467px;top:583px">★★★★★</div>
    <div class="abs reviews" style="left:471px;top:595px">1 Review(s)</div>

    <div class="abs footer">
      <span>WEFOLKLY powered by Meridian Trust Group Limited © · English (US)</span>
      <span class="footer__links"><span>About</span><span>Privacy</span><span>Invite</span><span>Terms</span><span>Contact Us</span><span>Developers</span><span>Affiliates</span></span>
    </div>
  </div>

  <div class="modal">
    <div class="modal__inner">
      <div class="modal__head">Map View</div>
      <div class="abs modal__field" style="left:9px;width:132px">Location...</div>
      <div class="abs modal__field" style="left:144px;width:120px">City...</div>
      <div class="abs modal__field" style="left:267px;width:92px">Radius...</div>
      <div class="abs modal__field" style="left:362px;width:33px">miles ▾</div>
      <div class="abs modal__map" role="img" aria-label="Street map of the city centre with two listing location pins"></div>
      <div class="abs modal__close">Close</div>
    </div>
  </div>

  <div class="copy">
    <h2 class="copy__title">Founding <span>(continued)</span></h2>
    <p>The vision was to further improve the economic and political situation of the southern part of Thailand through the website. The founders impressed upon the Muslim business associations in those regions about the potential of internet and how it can be a turning point for both the insurgency as well as to promote Thailand’s <em>halal</em> suppliers, which ranks the 5th largest <em>halal</em> export in the world and is of high standard.</p>
    <p>The Government for the Kingdom of Thailand later supported the project in line of their Digital Economy policy. The website was launched on 28th December at the inaugural Thailand <em>Halal</em> Expo by the Prime Minister of Thailand, General Arun Sakdichai.</p>
  </div>
  <div class="folio">9</div>
</div>
</body>
</html>
```